Modern Innovative Business Card Design

We require a nice, modern, clean business card design, ready for upload to Cardomora. Our company develops online banking software solutions for small financial insitutions. The design should be clean, professional, but yet not "corporate boring". See www.fyrolt.com for an idea of business image and profile. The design should communicate innovation, be modern and fresh, yet look professional and established.

Target Market(s)

Finance industry, bankers, entrepreneurs

Industry/Entity Type

Financial

Contact Information for Business Card

Tobias Wendlerup
CEO

FYROLT BV
Lindenwerf 38
1027 HX Amsterdam
The Netherlands

Phone: +31 20 517 8036
Direct: +31 20 604 1758
Skype: tobias.fyrolt
ceo@fyrolt.com
www.fyrolt.com

Font styles to use
Sans Serif

Requirements
Must have
• Should look clean, modern and professional. File should be ready for upload to cardomora.
Should not have
• Boring standard corporate layout

```html
<!DOCTYPE html>
<html lang="en">
<head>
<meta charset="utf-8">
<title>FYROLT business card concepts</title>
<link rel="stylesheet" href="https://fonts.googleapis.com/css2?family=Arimo:wght@400;700&family=Tinos:wght@700&display=swap">
<style>
:root{
  --green:#8dc21f;
  --green-dark:#79a81a;
  --ink:#58595b;
  --ink-soft:#8a8b8d;
  --frame:#5d5e60;
  --paper:#ffffff;
  --bg:#ffffff;
}
*{box-sizing:border-box;margin:0;padding:0}
html,body{width:1200px;height:900px;overflow:hidden;background:var(--bg)}
body{position:relative;font-family:"Arimo",Arial,sans-serif;color:var(--ink)}
.card{position:absolute;background:var(--paper);box-shadow:3px 4px 9px rgba(0,0,0,.38);overflow:hidden}
.h{width:279px;height:157px}
.v{width:157px;height:279px}
.el{position:absolute}
.logo{font-weight:700;color:var(--ink);font-size:31px;letter-spacing:2px;line-height:1}
.logo.sm{font-size:27px}
.name{font-weight:700;font-size:11.5px;line-height:1;text-transform:uppercase;color:var(--ink);white-space:nowrap}
.name.green{color:var(--green)}
.title{font-weight:700;font-size:7px;color:var(--green);line-height:1;margin-top:2px;padding-left:4px;letter-spacing:.3px}
.title.gray{color:var(--ink)}
.info{font-size:6.6px;line-height:8px;color:var(--ink);white-space:nowrap}
.info.soft{color:var(--ink-soft)}
.info.green{color:var(--green)}
.info p+p{margin-top:0}
.gap{height:7px}
.rule{height:1.5px;background:var(--ink);width:74px;margin:2px 0}
.center{text-align:center}
svg{position:absolute;display:block}
</style>
</head>
<body>

<!-- Column 1 -->
<section class="card h" style="left:114px;top:5px">
  <div class="el" style="right:10px;top:7px;text-align:right">
    <div class="name green">Tobias Wendlerup</div>
    <div class="title gray" style="padding-right:34px">CEO FYROLT</div>
  </div>
  <div class="el logo" style="left:10px;top:64px">FYROLT</div>
  <div class="el info soft" style="left:10px;top:126px"><p>BV Lindenwerf</p><p>38 1027 HX Amsterdam</p><p>The Netherlands</p></div>
  <div class="el info soft" style="left:108px;top:126px"><p>www.fyrolt.com</p><p>ceo@fyrolt.com</p><p>Skype: tobias.fyrolt</p></div>
  <div class="el info soft" style="left:204px;top:134px"><p>Phone: +31 20 517 8036</p><p>Direct: +31 20 604 1758</p></div>
</section>

<section class="card h" style="left:114px;top:190px">
  <div class="el" style="left:8px;top:8px"><div class="name">Tobias Wendlerup</div><div class="title" style="padding-left:28px">CEO FYROLT</div></div>
  <div class="el" style="left:156px;top:50px;width:3px;height:82px;background:var(--green)"></div>
  <div class="el logo" style="left:5px;top:78px">FYROLT</div>
  <div class="el info green" style="left:176px;top:50px"><p>BV Lindenwerf</p><p>38 1027 HX Amsterdam</p><p>The Netherlands</p><div class="gap"></div><p>Phone: +31 20 517 8036</p><p>Direct: +31 20 604 1758</p><div class="gap"></div><p>www.fyrolt.com</p><p>ceo@fyrolt.com</p><p>Skype: tobias.fyrolt</p></div>
</section>

<section class="card h" style="left:114px;top:377px">
  <div class="el" style="left:10px;top:10px"><div class="name">Tobias Wendlerup</div><div class="title">CEO FYROLT</div></div>
  <div class="el info" style="left:10px;top:76px"><p>BV Lindenwerf</p><p>38 1027 HX Amsterdam</p><p>The Netherlands</p><div class="rule"></div><p>Phone: +31 20 517 8036</p><p>Direct: +31 20 604 1758</p><div class="rule"></div><p>www.fyrolt.com</p><p>ceo@fyrolt.com</p><p>Skype: tobias.fyrolt</p></div>
  <div class="el logo" style="left:128px;top:76px">FYROLT</div>
</section>

<section class="card h" style="left:114px;top:557px">
  <div class="el logo" style="left:128px;top:10px">FYROLT</div>
  <div class="el info" style="left:10px;top:78px"><p>BV Lindenwerf</p><p>38 1027 HX Amsterdam</p><p>The Netherlands</p><div class="rule"></div><p>Phone: +31 20 517 8036</p><p>Direct: +31 20 604 1758</p><div class="rule"></div><p>www.fyrolt.com</p><p>ceo@fyrolt.com</p><p>Skype: tobias.fyrolt</p></div>
</section>

<section class="card h" style="left:114px;top:739px">
  <div class="el" style="left:10px;top:0;width:75px;height:31px;background:var(--green)"></div>
  <div class="el" style="right:6px;top:6px;text-align:right"><div class="name">Tobias Wendlerup</div><div class="title" style="padding-right:50px">CEO FYROLT</div></div>
  <div class="el logo" style="left:136px;top:66px">FYROLT</div>
  <div class="el info green" style="left:10px;top:76px"><p>BV Lindenwerf</p><p>38 1027 HX Amsterdam</p><p>The Netherlands</p><div class="rule" style="background:var(--green)"></div><p>Phone: +31 20 517 8036</p><p>Direct: +31 20 604 1758</p><div class="rule" style="background:var(--green)"></div><p>www.fyrolt.com</p><p>ceo@fyrolt.com</p><p>Skype: tobias.fyrolt</p></div>
</section>

<!-- Column 2 -->
<section class="card h" style="left:418px;top:5px;width:272px">
  <div class="el logo" style="left:128px;top:12px">FYROLT</div>
  <div class="el" style="left:8px;top:92px"><div class="name">Tobias Wendlerup</div><div class="title">CEO FYROLT</div></div>
  <div class="el info" style="left:8px;top:128px"><p>BV Lindenwerf</p><p>38 1027 HX Amsterdam</p><p>The Netherlands</p></div>
  <div class="el info" style="left:102px;top:128px"><p>www.fyrolt.com</p><p>ceo@fyrolt.com</p><p>Skype: tobias.fyrolt</p></div>
  <div class="el info" style="left:195px;top:136px"><p>Phone: +31 20 517 8036</p><p>Direct: +31 20 604 1758</p></div>
</section>

<section class="card h" style="left:411px;top:190px">
  <div class="el logo" style="left:10px;top:10px">FYROLT</div>
  <div class="el" style="left:6px;top:78px"><div class="name">Tobias Wendlerup</div><div class="title">CEO FYROLT</div></div>
  <div class="el info" style="left:6px;top:126px"><p>BV Lindenwerf</p><p>38 1027 HX Amsterdam</p><p>The Netherlands</p></div>
  <div class="el info" style="left:101px;top:126px"><p>www.fyrolt.com</p><p>ceo@fyrolt.com</p><p>Skype: tobias.fyrolt</p></div>
  <div class="el info" style="left:194px;top:134px"><p>Phone: +31 20 517 8036</p><p>Direct: +31 20 604 1758</p></div>
  <div class="el" style="left:0;bottom:0;width:100%;height:3px;background:var(--green)"></div>
</section>

<section class="card h" style="left:411px;top:377px">
  <div class="el" style="left:10px;top:10px"><div class="name">Tobias Wendlerup</div><div class="title">CEO FYROLT</div></div>
  <div class="el" style="left:177px;top:70px;width:1px;height:78px;background:#ccc"></div>
  <div class="el info" style="left:191px;top:70px"><p>BV Lindenwerf</p><p>38 1027 HX Amsterdam</p><p>The Netherlands</p><div class="gap"></div><p>Phone: +31 20 517 8036</p><p>Direct: +31 20 604 1758</p><div class="gap"></div><p>www.fyrolt.com</p><p>ceo@fyrolt.com</p><p>Skype: tobias.fyrolt</p></div>
  <div class="el logo" style="left:8px;top:122px">FYROLT</div>
</section>

<section class="card h" style="left:411px;top:554px">
  <div class="el logo" style="left:8px;top:10px">FYROLT</div>
  <div class="el info" style="left:198px;top:66px"><p>BV Lindenwerf</p><p>38 1027 HX Amsterdam</p><p>The Netherlands</p><div class="gap"></div><p>Phone: +31 20 517 8036</p><p>Direct: +31 20 604 1758</p><div class="gap"></div><p>www.fyrolt.com</p><p>ceo@fyrolt.com</p><p>Skype: tobias.fyrolt</p></div>
  <div class="el" style="left:8px;top:130px"><div class="name" style="font-family:'Tinos',serif;text-transform:none;font-size:12px">Tobias Wendlerup</div><div class="title" style="padding-left:0">CEO FYROLT</div></div>
</section>

<section class="card h" style="left:418px;top:739px;width:280px">
  <div class="el" style="left:10px;top:7px"><div style="font-size:14px;line-height:1;color:var(--ink)">Tobias Wendlerup</div><div class="title" style="padding-left:0">CEO FYROLT</div></div>
  <div class="el info" style="left:200px;top:50px;font-size:5px;line-height:6px"><p>BV Lindenwerf</p><p>38 1027 HX Amsterdam</p><div class="gap"></div><p>Phone: +31 20 517 8036</p><p>Direct: +31 20 604 1758</p><div class="gap"></div><p>www.fyrolt.com</p><p>ceo@fyrolt.com</p><p>Skype: tobias.fyrolt</p></div>
  <div class="el logo" style="left:15px;top:100px">FYROLT</div>
  <div class="el" style="left:265px;top:0;width:1px;height:100%;background:var(--green)"></div>
  <div class="el" style="left:272px;top:0;width:8px;height:100%;background:var(--green)"></div>
</section>

<!-- Column 3 -->
<section class="card v" style="left:714px;top:5px">
  <svg width="157" height="135" viewBox="0 0 157 135" aria-hidden="true">
    <polygon points="0,0 157,0 157,50" fill="var(--green)"/>
    <polygon points="55,0 157,0 157,120 " fill="var(--green-dark)" opacity=".8"/>
    <polygon points="0,0 60,0 0,50" fill="var(--green)" opacity=".75"/>
    <polygon points="60,40 157,0 157,135" fill="var(--green)"/>
  </svg>
  <div class="el" style="left:9px;top:92px"><div class="name">Tobias Wendlerup</div></div>
  <div class="el info" style="left:9px;top:122px"><p>BV Lindenwerf</p><p>38 1027 HX Amsterdam</p><p>The Netherlands</p><div class="gap"></div><p>Phone: +31 20 517 8036</p><p>Direct: +31 20 604 1758</p><div class="gap"></div><p>www.fyrolt.com</p><p>ceo@fyrolt.com</p><p>Skype: tobias.fyrolt</p></div>
  <div class="el logo sm" style="left:9px;top:240px">FYROLT</div>
</section>

<section class="card v" style="left:719px;top:299px;width:158px">
  <div class="el logo sm" style="left:9px;top:14px">FYROLT</div>
  <div class="el" style="left:9px;top:38px;width:48px;height:2px;background:var(--ink)"></div>
  <div class="el" style="left:9px;top:132px"><div class="name">Tobias Wendlerup</div><div class="title">CEO FYROLT</div></div>
  <div class="el" style="left:9px;top:158px;width:48px;height:3px;background:var(--green)"></div>
  <div class="el info" style="left:9px;top:166px"><p>BV Lindenwerf</p><p>38 1027 HX Amsterdam</p><p>The Netherlands</p><div class="gap"></div><p>Phone: +31 20 517 8036</p><p>Direct: +31 20 604 1758</p><div class="gap"></div><p>www.fyrolt.com</p><p>ceo@fyrolt.com</p><p>Skype: tobias.fyrolt</p></div>
  <svg width="158" height="70" viewBox="0 0 158 70" style="left:0;bottom:0" aria-hidden="true">
    <polygon points="80,70 158,10 158,70" fill="var(--green-dark)"/>
    <polygon points="60,70 158,40 158,70" fill="var(--green)"/>
  </svg>
</section>

<section class="card v" style="left:723px;top:609px;width:157px;height:279px;border:6px solid var(--frame)">
  <div class="el logo sm" style="left:6px;top:10px">FYROLT</div>
  <div class="el center" style="left:0;right:0;top:126px"><div class="name">Tobias Wendlerup</div><div class="title" style="padding-left:0">CEO FYROLT</div></div>
  <div class="el info center" style="left:0;right:0;top:184px"><p>BV Lindenwerf</p><p>38 1027 HX Amsterdam</p><p>The Netherlands</p><div class="gap"></div><p>Phone: +31 20 517 8036</p><p>Direct: +31 20 604 1758</p><div class="gap"></div><p>www.fyrolt.com</p><p>ceo@fyrolt.com</p><p>Skype: tobias.fyrolt</p></div>
</section>

<!-- Column 4 -->
<section class="card v" style="left:918px;top:5px">
  <div class="el" style="left:11px;top:12px"><div class="name">Tobias Wendlerup</div><div class="title">CEO FYROLT</div></div>
  <div class="el logo sm" style="left:9px;top:95px">FYROLT</div>
  <div class="el" style="left:11px;top:158px;width:26px;height:4px;background:var(--green)"></div>
  <div class="el info" style="left:9px;top:191px"><p>BV Lindenwerf</p><p>38 1027 HX Amsterdam</p><p>The Netherlands</p><div class="gap"></div><p>Phone: +31 20 517 8036</p><p>Direct: +31 20 604 1758</p><div class="gap"></div><p>www.fyrolt.com</p><p>ceo@fyrolt.com</p><p>Skype: tobias.fyrolt</p></div>
</section>

<section class="card v" style="left:918px;top:305px">
  <div class="el" style="left:0;top:0;width:100%;height:15px;background:var(--green)"></div>
  <div class="el" style="left:9px;top:32px"><div class="name">Tobias Wendlerup</div><div class="title">CEO FYROLT</div></div>
  <div class="el logo sm" style="left:9px;top:108px">FYROLT</div>
  <div class="el info" style="left:9px;top:190px"><p>BV Lindenwerf</p><p>38 1027 HX Amsterdam</p><p>The Netherlands</p><div class="gap"></div><p>Phone: +31 20 517 8036</p><p>Direct: +31 20 604 1758</p><div class="gap"></div><p>www.fyrolt.com</p><p>ceo@fyrolt.com</p><p>Skype: tobias.fyrolt</p></div>
</section>

<section class="card v" style="left:918px;top:605px">
  <div class="el logo sm" style="left:9px;top:18px">FYROLT</div>
  <div class="el" style="left:11px;top:90px"><div class="name">Tobias Wendlerup</div><div class="title">CEO FYROLT</div></div>
  <div class="el info" style="left:9px;top:165px"><p>BV Lindenwerf</p><p>38 1027 HX Amsterdam</p><p>The Netherlands</p><div class="rule" style="width:38px"></div><p>Phone: +31 20 517 8036</p><p>Direct: +31 20 604 1758</p><div class="rule" style="width:38px"></div><p>www.fyrolt.com</p><p>ceo@fyrolt.com</p><p>Skype: tobias.fyrolt</p><div class="rule" style="width:74px"></div></div>
  <div class="el" style="right:18px;bottom:0;width:10px;height:10px;background:var(--frame)"></div>
</section>

</body>
</html>
```